Local Horticulturalist needs Business card design

Meridale Gardening would like to update our existing business card and utilize our new logo (design attached)....we specialize in getting the best out of our customers yard with professional maintenance programs, expert pruning and hedging and garden restorations.
Utilizing colors from attached logo I would like a design that implies professionalism and if possible our businesses love of restoration through plants.
I also sometimes write down for my customers a start date and price on the back of my current card
Target Market(s)
Home owners
Contractors
Industry/Entity Type
Gardener
Contact Information for Business Card
Trevor Kalbrook | Horticulturalist
ph: 0452739186
meridalegard@fernpost.com
www.meridalegardening.com.au
Requirements
Must have
- crucial information easy to read
- incorporate current logo
- Horticulturalist listed preferably near name
Nice to have
- currently I write a job start date and price on the back of my current card so something that integrates this would be beneficial
Should not have
- be pretty or flowerey
- be too white or basic

```html
<!DOCTYPE html>
<html lang="en">
<head>
<meta charset="utf-8">
<title>Meridale Gardening — Business Card</title>
<link href="https://fonts.googleapis.com/css2?family=Arimo:wght@400;700&display=swap" rel="stylesheet">
<style>
  :root {
    --leaf-green: #8dc63f;
    --soil-brown: #7e6d55;
    --tint-green: #e6f1cf;
    --charcoal: #222220;
    --dash-grey: #9a9a9a;
    --contact-brown: #a08e70;
    --page: #ffffff;
  }
  * { margin: 0; padding: 0; box-sizing: border-box; }
  html, body { width: 1200px; height: 968px; overflow: hidden; background: var(--page); }
  body { position: relative; font-family: "Arimo", Arial, sans-serif; }

  .card {
    position: absolute;
    left: 323px;
    width: 549px;
    height: 311px;
    background: linear-gradient(160deg, var(--tint-green) 0%, #f6faee 40%, #ffffff 70%);
    border: 1px solid #b5b5b5;
    box-shadow: 8px 9px 10px rgba(0,0,0,0.22);
    overflow: hidden;
  }
  .card--back { top: 108px; }
  .card--front { top: 515px; }

  .brand {
    position: absolute;
    left: 70px;
    top: 62px;
    display: flex;
    align-items: center;
    gap: 14px;
  }
  .brand__dot {
    width: 88px; height: 88px; border-radius: 50%;
    background: var(--leaf-green);
    flex: none;
  }
  .brand__name {
    font-size: 29px; font-weight: 700; color: var(--soil-brown);
    line-height: 1; letter-spacing: -0.2px;
  }
  .brand__tagline {
    margin-top: 4px;
    font-size: 14px; color: var(--soil-brown); letter-spacing: 0.4px;
  }

  .rule { position: absolute; left: 0; width: 100%; height: 6px; background: var(--leaf-green); }
  .card--back .rule { top: 213px; }
  .card--front .rule { top: 192px; }

  .notes { position: absolute; left: 0; top: 219px; width: 100%; height: 61px; background: #fff; }
  .notes__line {
    position: absolute; left: 37px; width: 474px; height: 0;
    border-top: 1.5px dashed var(--dash-grey);
  }
  .notes__line--date { top: 19px; }
  .notes__line--price { top: 42px; }

  .footer-band { position: absolute; left: 0; bottom: 0; width: 100%; height: 31px; }

  .details {
    position: absolute; left: 0; top: 198px; width: 100%; height: 113px;
    background: var(--charcoal);
  }
  .person { position: absolute; left: 22px; top: 23px; }
  .person__name { font-size: 25px; font-weight: 700; color: var(--leaf-green); letter-spacing: 0.3px; }
  .person__role { margin-top: 8px; font-size: 20px; color: var(--soil-brown); }

  .contacts { position: absolute; left: 312px; top: 28px; list-style: none; }
  .contacts li {
    display: flex; align-items: center; gap: 13px;
    height: 20.5px; font-size: 11px; color: var(--contact-brown);
  }
  .contacts svg { width: 20px; height: 16px; flex: none; }
</style>
</head>
<body>

  <section class="card card--back" aria-label="Card back with job notes">
    <div class="brand">
      <span class="brand__dot"></span>
      <div>
        <div class="brand__name">Meridale Gardening</div>
        <div class="brand__tagline">Garden Restorations &amp; Maintenance</div>
      </div>
    </div>
    <div class="rule"></div>
    <div class="notes">
      <div class="notes__line notes__line--date"></div>
      <div class="notes__line notes__line--price"></div>
    </div>
    <svg class="footer-band" viewBox="0 0 549 31" preserveAspectRatio="none">
      <rect width="549" height="31" fill="var(--leaf-green)"/>
      <polygon points="0,0 240,0 270,31 0,31" fill="var(--soil-brown)"/>
    </svg>
  </section>

  <section class="card card--front" aria-label="Card front with contact details">
    <div class="brand">
      <span class="brand__dot"></span>
      <div>
        <div class="brand__name">Meridale Gardening</div>
        <div class="brand__tagline">Garden Restorations &amp; Maintenance</div>
      </div>
    </div>
    <div class="rule"></div>
    <div class="details">
      <div class="person">
        <div class="person__name">Trevor Kalbrook</div>
        <div class="person__role">Horticulturalist</div>
      </div>
      <ul class="contacts">
        <li>
          <svg viewBox="0 0 20 16" aria-hidden="true">
            <path d="M2 5 Q10 0 18 5 L18 7 L14 7 L14 5 L6 5 L6 7 L2 7 Z" fill="var(--soil-brown)"/>
            <rect x="4" y="8" width="12" height="7" rx="1" fill="var(--soil-brown)"/>
          </svg>
          <span>0452739186</span>
        </li>
        <li>
          <svg viewBox="0 0 20 16" aria-hidden="true">
            <rect x="2" y="3" width="16" height="11" fill="var(--soil-brown)"/>
            <polyline points="2,3 10,10 18,3" fill="none" stroke="var(--charcoal)" stroke-width="1.3"/>
          </svg>
          <span>meridalegard@fernpost.com</span>
        </li>
        <li>
          <svg viewBox="0 0 20 16" aria-hidden="true">
            <g fill="none" stroke="var(--soil-brown)" stroke-width="1.4">
              <circle cx="10" cy="8" r="6.5"/>
              <ellipse cx="10" cy="8" rx="3" ry="6.5"/>
              <line x1="3.5" y1="8" x2="16.5" y2="8"/>
            </g>
          </svg>
          <span>www.meridalegardening.com.au</span>
        </li>
      </ul>
    </div>
  </section>

</body>
</html>
```